Realtor Just Listed Postcard Redesign

We need the existing postcard redesigned to fit on a 5x7 postcard.

Most importantly, we need the new postcard to be designed within a user friendly template system (PDF etc) that will allow us to change certain elements of the postcard (Front: photo Back: text information and photos). I've included additional previous design files as well.

Industry/Entity Type

Realtor

Requirements
Must have
• Template

```html
<!DOCTYPE html>
<html lang="en">
<head>
<meta charset="utf-8">
<title>Open House Postcard</title>
<link href="https://fonts.googleapis.com/css2?family=Open+Sans:wght@400;600;700;800&display=swap" rel="stylesheet">
<style>
:root{
  --navy:#1f3a63;
  --navy-dark:#16294a;
  --ink:#1d2430;
  --white:#ffffff;
  --backdrop:#2a2624;
  --red:#c8202f;
}
*{box-sizing:border-box;margin:0;padding:0}
html,body{width:900px;height:1200px;overflow:hidden;background:var(--backdrop);font-family:"Open Sans",Arial,sans-serif;color:var(--ink)}
.canvas{position:relative;width:900px;height:1200px}
.card{position:absolute;left:36px;width:828px;background:var(--white);overflow:hidden;box-shadow:0 6px 18px rgba(0,0,0,.45)}
.front{top:84px;height:548px}
.back{top:648px;height:530px}

/* front */
.front-band{position:absolute;left:0;top:0;width:828px;height:380px;display:block}
.headline{position:absolute;left:34px;top:22px;color:var(--white);font-weight:800;font-size:50px;line-height:1.1;letter-spacing:-.5px}
.hero-photo{position:absolute;left:30px;top:136px;width:300px;height:214px;border:8px solid var(--white);background:linear-gradient(160deg,#f4efe8,#d9cfc4 60%,#b8a79a)}
.agent-photo{position:absolute;right:0;top:40px;width:260px;height:290px;background:linear-gradient(180deg,#4a5668,#2c3340 55%,#1c2029)}
.name-box{position:absolute;left:538px;top:218px;background:var(--white);padding:6px 16px 8px;box-shadow:0 2px 6px rgba(0,0,0,.25)}
.name-box .role,.name-box .name{display:block;color:var(--ink);font-weight:600;font-size:30px;line-height:1.1}
.contact{position:absolute;right:34px;top:346px;color:var(--navy);font-weight:700;line-height:1.35;text-align:right}
.contact .phone{font-size:24px}
.contact .mail{font-size:14px}
.brand{position:absolute;left:32px;top:440px}
.brand-name{display:flex;align-items:center;gap:8px;color:var(--navy);font-weight:800;font-size:26px}
.brand-name i{width:18px;height:18px;background:var(--red);border-radius:50%;display:block}
.brand-note{margin-top:4px;font-size:10px;color:var(--ink);line-height:1.35}

/* back */
.invite{position:absolute;left:0;right:0;top:10px;text-align:center;color:var(--navy)}
.invite h1{font-weight:600;font-size:30px}
.invite .address{font-size:19px;font-weight:600;color:var(--ink)}
.invite .when{font-size:22px;font-weight:800;color:var(--ink)}
.tag{position:absolute;font-weight:800;font-size:20px;color:var(--navy)}
.tag.just{left:14px;top:70px}
.tag.sold{right:30px;top:70px}
.thumb{position:absolute;width:96px;height:74px;background:linear-gradient(150deg,#d9d2c8,#9c8f80)}
.thumb.a{left:14px;top:108px}
.thumb.b{left:14px;top:190px;background:linear-gradient(150deg,#e6ddd0,#a88e70)}
.thumb.c{left:14px;top:272px;background:linear-gradient(150deg,#cfd4d8,#7d8a93)}
.more{position:absolute;left:14px;top:352px;font-size:10px;line-height:1.3;color:var(--ink)}
.facts{position:absolute;left:122px;top:108px;width:130px;font-size:13px;line-height:1.55;font-weight:700;color:var(--ink)}
.facts li{list-style:none}
.blurb{position:absolute;left:268px;top:108px;width:300px;font-size:14px;line-height:1.5;color:var(--ink)}
.sold-photo{position:absolute;right:30px;width:200px;height:108px;background:linear-gradient(160deg,#b7c5a7,#6f7f5b)}
.sold-photo.a{top:106px}
.sold-photo.b{top:222px;background:linear-gradient(160deg,#c9c1b3,#7d6d5c)}
.sold-photo.c{top:338px;background:linear-gradient(160deg,#aebdc7,#5f6f79)}
.footer{position:absolute;left:0;right:0;bottom:0;height:62px;background:var(--navy);color:var(--white)}
.follow{position:absolute;left:430px;top:8px;font-size:12px}
.socials{position:absolute;left:430px;top:28px;display:flex;gap:8px}
.socials span{width:24px;height:24px;border-radius:50%;background:var(--white);display:block}
.office{position:absolute;left:572px;top:7px;font-size:9.5px;line-height:1.3;width:250px}
.office strong{font-size:11px}
</style>
</head>
<body>
<div class="canvas">

  <section class="card front">
    <svg class="front-band" viewBox="0 0 828 380" preserveAspectRatio="none" aria-hidden="true">
      <path d="M0 0H828V340C720 356 650 322 560 342C440 368 340 330 230 352C140 370 60 340 0 360Z" fill="var(--navy)"/>
    </svg>
    <h1 class="headline">You don’t want to<br>miss this!</h1>
    <div class="hero-photo" role="img" aria-label="Photo of the listed home's living room"></div>
    <div class="agent-photo" role="img" aria-label="Portrait of the realtor"></div>
    <div class="name-box"><span class="role">REALTOR</span><span class="name">MARCUS</span></div>
    <div class="contact">
      <div class="phone">(555) 214-0390</div>
      <div class="mail">marcus@realtormarcus.com</div>
      <div class="mail">www.realtormarcus.com</div>
    </div>
    <div class="brand">
      <div class="brand-name"><i></i>Summit Realty</div>
      <p class="brand-note">Summit Select Properties<br>Each office independently owned and operated</p>
    </div>
  </section>

  <section class="card back">
    <header class="invite">
      <h1>You’re invited to an Open House</h1>
      <p class="address">418 Harbour Crest Way is open on</p>
      <p class="when">May 5th &amp; 6th, 2-4PM</p>
    </header>

    <div class="tag just">Just Listed</div>
    <div class="thumb a" role="img" aria-label="Listing photo of the kitchen"></div>
    <div class="thumb b" role="img" aria-label="Listing photo of the bedroom"></div>
    <div class="thumb c" role="img" aria-label="Listing photo of the building exterior"></div>
    <p class="more">More Photo @<br>www.realtormarcus.com</p>

    <ul class="facts">
      <li>Harbour Crest Way</li>
      <li>Westbrook</li>
      <li>MLS#: V512846</li>
      <li>Type: Apartment</li>
      <li>List Price: $414,900</li>
      <li>Bedrooms: 2</li>
      <li>Bathrooms: 2</li>
      <li>Sq. Feet: 975</li>
      <li>Taxes: $1,341 (2011)</li>
      <li>Year Built: 1972</li>
    </ul>

    <p class="blurb">Beautiful southeast corner suite with private entrance! Huge, sunny, fully fenced private patio (582 sqft) on the quiet side of the bldg. Cleverly distributed spacious living area with open concept gourmet kitchen, new black &amp; stainless appliances, wainscotings, crown moulding, pecan hardwood saving, and generous master bedroom. Well managed building with new front entrance and updated roof &amp; piping. Parking &amp; storage locker included. Visit the listing Realtor’s website for more photos and open plan.</p>

    <div class="tag sold">Recently Sold:</div>
    <div class="sold-photo a" role="img" aria-label="Photo of a recently sold house"></div>
    <div class="sold-photo b" role="img" aria-label="Photo of a recently sold townhouse"></div>
    <div class="sold-photo c" role="img" aria-label="Photo of a recently sold apartment building"></div>

    <footer class="footer">
      <span class="follow">Follow me on:</span>
      <div class="socials"><span></span><span></span><span></span><span></span></div>
      <p class="office"><strong>Summit Select Realty</strong><br>1200 Cedar Ave. Westbrook, BC V0V 0A0<br>Each Office Independently Owned &amp; Operated.<br>Not meant to breach any agency agreement.</p>
    </footer>
  </section>

</div>
</body>
</html>
```